Bluefin Coatings Stationary Set

looking for the full stationary set including business card. Looking for it to be clean but edgy. I attached the logo and would like to see all the colors options in the design.

Vanity #:
844-TRY-BLUEFIN
844-317-5296

Slogan:
We Got You Covered

As far as personal name, title. lic# address - I would like to be able to change this on my own.

For Now:
Dale Hutchmoor-Owner
4817 Larkspur Lane
San Jose,CA 95137

estimates@bluefincoatings.example
www.bluefincoatings.example

Target Market(s)

Construction-Custom Homes, multi-family, residential and commercial

Industry/Entity Type

Painting And Decorating

Requirements
Must have
• Looking for/
• Business Card
• Letterhead
• Envelope
• Folder
• Or any additional suggestive items to make a more complete package
Nice to have
• Thank you card, fax coversheet, invoice
Should not have
• Notebooks, pens/pencils, erasers, cups/mugs key chains.

```html
<!DOCTYPE html>
<html lang="en">
<head>
<meta charset="utf-8">
<title>Bluefin Coatings Stationery Set</title>
<link href="https://fonts.googleapis.com/css2?family=Montserrat:wght@400;500;600;700&family=Open+Sans:wght@400;600&display=swap" rel="stylesheet">
<style>
  :root {
    --backdrop: #e8e8e8;
    --paper: #f7f7f7;
    --charcoal: #5e5e5e;
    --charcoal-dark: #4f4f4f;
    --leaf: #57a531;
    --ink: #555555;
    --ink-light: #8a8a8a;
    --white: #ffffff;
  }
  * { box-sizing: border-box; margin: 0; padding: 0; }
  html, body { width: 1200px; height: 890px; overflow: hidden; }
  body {
    background: var(--backdrop);
    font-family: "Open Sans", Arial, sans-serif;
    color: var(--ink);
    position: relative;
  }
  .piece { position: absolute; background: var(--paper); box-shadow: 0 2px 6px rgba(0,0,0,.12); overflow: hidden; }

  /* brand name */
  .brand { display: flex; align-items: center; gap: 6px; font-family: "Montserrat", Arial, sans-serif; font-weight: 700; color: var(--charcoal); letter-spacing: .5px; white-space: nowrap; }
  .brand-dot { width: 1em; height: 1em; border-radius: 50%; background: var(--leaf); flex: none; }
  .brand--light { color: var(--white); }

  .photo-fill { position: absolute; background: linear-gradient(160deg, rgba(255,255,255,.12), rgba(255,255,255,.04)); }

  /* letterhead */
  .letterhead { left: 30px; top: 30px; width: 330px; height: 467px; }
  .letterhead .brand { position: absolute; left: 28px; top: 34px; font-size: 15px; }
  .letter-body { position: absolute; left: 28px; top: 88px; width: 274px; font-size: 7px; line-height: 1.55; color: var(--ink); }
  .letter-body .recipient { font-weight: 600; margin-bottom: 14px; }
  .letter-body p { margin-bottom: 8px; }
  .signature { width: 70px; height: 22px; background: linear-gradient(90deg, rgba(60,80,170,.18), rgba(60,80,170,.05)); border-radius: 3px; margin: 4px 0; }
  .letterhead-footer { position: absolute; left: 0; bottom: 0; width: 100%; }
  .letterhead-footer .bar { background: var(--charcoal); color: var(--white); font-size: 6.3px; padding: 6px 14px; display: flex; justify-content: space-between; font-family: "Montserrat", Arial, sans-serif; white-space: nowrap; }
  .letterhead-footer .stripe { height: 5px; background: var(--leaf); }

  /* folder */
  .folder { left: 390px; top: 30px; width: 330px; height: 467px; }
  .folder .brand { position: absolute; left: 50%; top: 44px; transform: translateX(-50%); font-size: 19px; }
  .folder-panel { position: absolute; left: 0; top: 120px; width: 100%; height: 347px; background: var(--charcoal); }
  .folder-panel .photo-fill { left: 70px; top: 0; width: 190px; height: 240px; }
  .folder-band { position: absolute; left: 0; bottom: 0; width: 100%; height: 92px; background: var(--leaf); }
  .folder-band .slogan { position: absolute; left: 22px; top: 38px; color: var(--white); font-size: 8px; font-weight: 600; font-family: "Montserrat", Arial, sans-serif; letter-spacing: .5px; }
  .folder-band .web { position: absolute; right: 22px; top: 38px; color: var(--white); font-size: 8px; font-family: "Montserrat", Arial, sans-serif; }

  /* envelope */
  .envelope { left: 750px; top: 30px; width: 420px; height: 210px; }
  .envelope-flap { position: absolute; left: 0; top: 0; width: 100%; height: 66px; background: var(--charcoal); border-radius: 0 0 18px 18px; display: flex; align-items: center; justify-content: center; }
  .envelope-flap .brand { font-size: 9px; }

  /* notepad */
  .notepad { left: 750px; top: 270px; width: 420px; height: 227px; }
  .notepad .photo-fill { right: 40px; top: 0; width: 170px; height: 120px; background: linear-gradient(160deg, rgba(0,0,0,.06), rgba(0,0,0,.02)); }
  .notepad .brand { position: absolute; left: 30px; top: 120px; font-size: 16px; }
  .notepad .address { position: absolute; left: 30px; bottom: 16px; font-size: 6.5px; color: var(--ink-light); font-family: "Montserrat", Arial, sans-serif; }
  .notepad-edge { position: absolute; right: 0; top: 0; height: 100%; display: flex; }
  .notepad-edge .green { width: 6px; background: var(--leaf); }
  .notepad-edge .grey { width: 12px; background: var(--charcoal); }

  /* business cards */
  .card { width: 330px; height: 185px; top: 540px; }
  .card-front { left: 230px; background: var(--charcoal); }
  .card-front .photo-fill { left: 22px; top: 0; width: 130px; height: 185px; }
  .card-front .brand { position: absolute; right: 30px; top: 78px; font-size: 15px; }
  .card-back { left: 640px; }
  .card-back .brand { position: absolute; left: 18px; top: 44px; font-size: 11px; }
  .card-person { position: absolute; left: 162px; top: 20px; width: 156px; font-family: "Montserrat", Arial, sans-serif; }
  .card-person .name { color: var(--leaf); font-weight: 700; font-size: 9px; text-transform: uppercase; letter-spacing: .4px; }
  .card-person .title { font-size: 7px; color: var(--ink-light); margin-bottom: 8px; }
  .contact-list { list-style: none; font-size: 6.6px; line-height: 1.9; color: var(--ink); }
  .contact-list li { display: flex; align-items: center; gap: 5px; white-space: nowrap; }
  .contact-list svg { width: 9px; height: 9px; flex: none; }
  .card-footer { position: absolute; left: 0; bottom: 0; width: 100%; }
  .card-footer .bar { background: var(--charcoal); color: var(--white); font-size: 6.5px; padding: 7px 18px; font-family: "Montserrat", Arial, sans-serif; }
  .card-footer .stripe { height: 5px; background: var(--leaf); }
</style>
</head>
<body>

  <!-- Letterhead -->
  <section class="piece letterhead" aria-label="Letterhead">
    <div class="brand"><span class="brand-dot"></span>Bluefin Coatings</div>
    <div class="letter-body">
      <div class="recipient">Recipient Name<br>Harbor Street 21<br>10115 Berlin<br>Germany</div>
      <p>Dear sir,</p>
      <p>Thank you for choosing us for your next project. Our crew brings careful preparation, clean lines and lasting finishes to every home and commercial space we touch.</p>
      <p>We plan each job around your schedule, protect your floors and furniture, and leave the site tidy at the end of every day.</p>
      <p>Please review the attached estimate and call us with any questions.</p>
      <p>Yours Sincerely,</p>
      <div class="signature" role="img" aria-label="Handwritten signature"></div>
      <p><strong>Tessa Morland</strong></p>
    </div>
    <div class="letterhead-footer">
      <div class="bar">
        <span>4817 Larkspur Lane, San Jose,CA 95137</span>
        <span>844-317-5296</span>
        <span>estimates@bluefincoatings.example</span>
      </div>
      <div class="stripe"></div>
    </div>
  </section>

  <!-- Presentation folder -->
  <section class="piece folder" aria-label="Presentation folder">
    <div class="brand"><span class="brand-dot"></span>Bluefin Coatings</div>
    <div class="folder-panel">
      <div class="photo-fill" role="img" aria-label="Faint photo of a painter holding a roller and paint bucket"></div>
      <div class="folder-band">
        <span class="slogan">We Got You Covered</span>
        <span class="web">www.bluefincoatings.example</span>
      </div>
    </div>
  </section>

  <!-- Envelope -->
  <section class="piece envelope" aria-label="Envelope back">
    <div class="envelope-flap">
      <div class="brand brand--light">Bluefin Coatings</div>
    </div>
  </section>

  <!-- Notepad -->
  <section class="piece notepad" aria-label="Notepad">
    <div class="photo-fill" role="img" aria-label="Faint photo of a painter holding a roller and paint bucket"></div>
    <div class="brand"><span class="brand-dot"></span>Bluefin Coatings</div>
    <div class="address">4817 Larkspur Lane, San Jose,CA 95137</div>
    <div class="notepad-edge"><span class="green"></span><span class="grey"></span></div>
  </section>

  <!-- Business card front -->
  <section class="piece card card-front" aria-label="Business card front">
    <div class="photo-fill" role="img" aria-label="Faint photo of a painter holding a roller and paint bucket"></div>
    <div class="brand brand--light">Bluefin Coatings</div>
  </section>

  <!-- Business card back -->
  <section class="piece card card-back" aria-label="Business card back">
    <div class="brand"><span class="brand-dot"></span>Bluefin Coatings</div>
    <div class="card-person">
      <div class="name">Dale Hutchmoor</div>
      <div class="title">Owner</div>
      <ul class="contact-list">
        <li>
          <svg viewBox="0 0 10 10"><path d="M2 1h2l1 2.5-1.2.8a5 5 0 0 0 2 2l.8-1.2L9 6v2a1 1 0 0 1-1 1A7 7 0 0 1 1 2a1 1 0 0 1 1-1z" fill="#57a531"/></svg>
          844-TRY-BLUEFIN
        </li>
        <li>
          <svg viewBox="0 0 10 10"><path d="M2 1h2l1 2.5-1.2.8a5 5 0 0 0 2 2l.8-1.2L9 6v2a1 1 0 0 1-1 1A7 7 0 0 1 1 2a1 1 0 0 1 1-1z" fill="#57a531"/></svg>
          844-317-5296
        </li>
        <li>
          <svg viewBox="0 0 10 10"><rect x="1" y="2" width="8" height="6" rx="1" fill="#57a531"/><path d="M1.5 2.5 5 5.5l3.5-3" stroke="#fff" stroke-width=".8" fill="none"/></svg>
          estimates@bluefincoatings.example
        </li>
        <li>
          <svg viewBox="0 0 10 10"><circle cx="5" cy="5" r="4" fill="none" stroke="#57a531" stroke-width="1"/><path d="M1 5h8M5 1c-2 2.5-2 5.5 0 8M5 1c2 2.5 2 5.5 0 8" stroke="#57a531" stroke-width=".7" fill="none"/></svg>
          www.bluefincoatings.example
        </li>
      </ul>
    </div>
    <div class="card-footer">
      <div class="bar">4817 Larkspur Lane, San Jose,CA 95137</div>
      <div class="stripe"></div>
    </div>
  </section>

</body>
</html>
```